Business card design

I need my logo on this card, things I need the card to have on it
licensed and insured.
owner operators Milo & Dexter Hartwell
my phone number 5558203146
Disaster Recovery, Storm Damage Restoration, Proactive Disaster Plan Management, Roof Repair/Restoration Structural Repair and Reconstruction, Emergency Boarding and Tarping Service, Perimeter Fencing, Emergency Tree Removal,

```html
<!DOCTYPE html>
<html lang="en">
<head>
<meta charset="utf-8">
<title>Hartwell's Construction — Business Card</title>
<link rel="stylesheet" href="https://fonts.googleapis.com/css2?family=Montserrat:wght@400;600;700&family=Lato:wght@400;700&display=swap">
<style>
  :root {
    --bg: #2a2a2c;
    --card: #1e1e1f;
    --panel: #161617;
    --blue: #1596ea;
    --grey: #6e6f73;
    --light: #e8e8e8;
    --white: #ffffff;
  }
  * { box-sizing: border-box; margin: 0; padding: 0; }
  html, body { width: 1200px; height: 875px; overflow: hidden; }
  body {
    background: var(--bg);
    position: relative;
    font-family: 'Lato', sans-serif;
  }
  .card {
    position: absolute;
    top: 277px;
    width: 560px;
    height: 320px;
    background: var(--card);
    border-radius: 18px;
    overflow: hidden;
  }
  .card--back { left: 27px; }
  .card--front { left: 613px; }

  /* Back: brand + services */
  .brand {
    position: absolute;
    left: 28px;
    top: 128px;
    width: 190px;
    color: var(--blue);
    font-family: 'Montserrat', sans-serif;
    font-weight: 400;
  }
  .brand__mark {
    width: 34px; height: 34px;
    background: var(--blue);
    margin: 0 0 12px 70px;
  }
  .brand__name { font-size: 27px; letter-spacing: 0.5px; line-height: 1; }
  .brand__sub { font-size: 9.5px; letter-spacing: 4.2px; margin-top: 6px; }
  .divider {
    position: absolute;
    left: 235px; top: 62px;
    width: 2px; height: 196px;
    background: var(--blue);
  }
  .services {
    position: absolute;
    left: 258px; top: 66px;
    list-style: none;
  }
  .services li {
    display: flex; align-items: center;
    color: var(--light);
    font-size: 13.5px;
    line-height: 23.5px;
  }
  .services svg { width: 14px; height: 14px; margin-right: 9px; flex: none; }

  /* Front: names + contact */
  .emblem {
    position: absolute;
    left: 18px; top: 100px;
    width: 270px; height: 200px;
    background: var(--panel);
    border-radius: 14px;
    display: flex; align-items: center; justify-content: center; gap: 12px;
    font-family: 'Montserrat', sans-serif;
    font-weight: 600;
    font-size: 24px;
    color: var(--blue);
  }
  .emblem__mark { width: 28px; height: 28px; background: var(--blue); }
  .contact {
    position: absolute;
    right: 34px; top: 30px;
    text-align: right;
    font-family: 'Montserrat', sans-serif;
  }
  .owners {
    color: var(--blue);
    font-weight: 700;
    font-size: 30px;
    line-height: 1.05;
    text-transform: uppercase;
  }
  .role { color: var(--grey); font-size: 16px; margin-top: 4px; }
  .rule { width: 26px; height: 2px; background: var(--blue); margin: 12px 0 12px auto; }
  .call { color: var(--white); font-weight: 700; font-size: 14px; font-family: 'Lato', sans-serif; }
  .phone { color: var(--white); font-weight: 700; font-size: 32px; font-family: 'Lato', sans-serif; line-height: 1.1; }
  .licence { color: var(--white); font-weight: 700; font-size: 15px; font-family: 'Lato', sans-serif; }
</style>
</head>
<body>
  <section class="card card--back">
    <div class="brand">
      <div class="brand__mark"></div>
      <div class="brand__name">HARTWELL'S</div>
      <div class="brand__sub">CONSTRUCTION L.L.C</div>
    </div>
    <div class="divider"></div>
    <ul class="services">
      <li><svg viewBox="0 0 14 14"><circle cx="7" cy="7" r="7" fill="#1596ea"/><path d="M3.8 7.2l2.2 2.1 4.2-4.4" fill="none" stroke="#1e1e1f" stroke-width="1.8"/></svg>Disaster Recovery</li>
      <li><svg viewBox="0 0 14 14"><circle cx="7" cy="7" r="7" fill="#1596ea"/><path d="M3.8 7.2l2.2 2.1 4.2-4.4" fill="none" stroke="#1e1e1f" stroke-width="1.8"/></svg>Storm Damage Restoration</li>
      <li><svg viewBox="0 0 14 14"><circle cx="7" cy="7" r="7" fill="#1596ea"/><path d="M3.8 7.2l2.2 2.1 4.2-4.4" fill="none" stroke="#1e1e1f" stroke-width="1.8"/></svg>Proactive Disaster Plan Management</li>
      <li><svg viewBox="0 0 14 14"><circle cx="7" cy="7" r="7" fill="#1596ea"/><path d="M3.8 7.2l2.2 2.1 4.2-4.4" fill="none" stroke="#1e1e1f" stroke-width="1.8"/></svg>Roof Repair / Restoration</li>
      <li><svg viewBox="0 0 14 14"><circle cx="7" cy="7" r="7" fill="#1596ea"/><path d="M3.8 7.2l2.2 2.1 4.2-4.4" fill="none" stroke="#1e1e1f" stroke-width="1.8"/></svg>Structural Repair &amp; Reconstruction</li>
      <li><svg viewBox="0 0 14 14"><circle cx="7" cy="7" r="7" fill="#1596ea"/><path d="M3.8 7.2l2.2 2.1 4.2-4.4" fill="none" stroke="#1e1e1f" stroke-width="1.8"/></svg>Emergency Boarding &amp; Tarping Service</li>
      <li><svg viewBox="0 0 14 14"><circle cx="7" cy="7" r="7" fill="#1596ea"/><path d="M3.8 7.2l2.2 2.1 4.2-4.4" fill="none" stroke="#1e1e1f" stroke-width="1.8"/></svg>Perimeter Fencing</li>
      <li><svg viewBox="0 0 14 14"><circle cx="7" cy="7" r="7" fill="#1596ea"/><path d="M3.8 7.2l2.2 2.1 4.2-4.4" fill="none" stroke="#1e1e1f" stroke-width="1.8"/></svg>Emergency Tree Removal</li>
    </ul>
  </section>

  <section class="card card--front">
    <div class="emblem">
      <span class="emblem__mark"></span>
      <span>HARTWELL'S</span>
    </div>
    <div class="contact">
      <h1 class="owners">Milo &amp;<br>Dexter<br>Hartwell</h1>
      <p class="role">Owner Operators</p>
      <div class="rule"></div>
      <p class="call">Call Us Today</p>
      <p class="phone">5558203146</p>
      <div class="rule"></div>
      <p class="licence">licensed &amp; insured</p>
    </div>
  </section>
</body>
</html>
```